Hosted PBX VoIP Web Site Redesign WordPress Template

We offer hosted 'in the cloud' telephone services. Our current site is http://www.brimwoodvoicelink.com and the site needs a major work-over. The site MUST BE be completed in WordPress as a template design.
I want this new site to have a warm look and feel giving the impression that we give the best customer service for small to medium businesses. The target business customer is small business with 5 to 50 employees with remote working employees who need to stay in communications with other staff.
Differentiation from our competitors is what we are looking for. We have been selling hosted pbx services for more than 7 years, we own our data center and have been in the data center business since 2000. Here are some examples of what I would like to have as a new web site:
Other hosted PBX companies:
http://www.quorvelo.com/
http://www.mendrix.com/
http://www.telbrandor.com/
http://www.glimber.com/
http://www.swiftlinecall.com/
Not Hosted PBX companies, but sites I like are:
http://www.kelvarnet.com/
http://www.zorquill.com/
http://www.plintbox.com/
I don't want a copy-cat web site and will invest in good graphics and original photography and graphics as needed.
Dana Worley
http://www.brimwoodweb.com
Updates
Here are some ideas I have look at. I want a very clean Word Press web site like these:
Other hosted PBX companies that we can get some graphic ideas from and good content.
http://www.quorvelo.com/
http://www.mendrix.com/
http://www.glimber.com/
http://www.swiftlinecall.com/
http://www.hablex.com/
http://www.quillpath.com/
http://www.kelvarnet.com/
http://www.zorquill.com/ - I like this clean design
http://www.plintbox.com/
I have engaged Vantor8.4 Media Group to make a video similar to this one to embed on our new home page, They did a good job with the copy and graphics on the http://www.Morvessa.com video. This is the video I want them to emulate http://www.biz.kelnotel.com/content/mixedmedia/TalkCore_H264.mp4 Watch this video. It tells what we do but on a smaller scale. We don't have the budget KLT has to do what they did.
When needed I will engage http://www.wordmintery.com to write come fresh new content work our new web site. That is why it's important that it be a good WordPress template that I can add news articles to for good SEO.
Dana
Target Market(s)
small business owners, business with tele or remote workers
Industry/Entity Type
Small Business
Requirements
Must have
- clean look and feel, easy to read. I might a video that explains our service. Here's what we do. Watch this video at http://www.biz.kelnotel.com/content/mixedmedia/TalkCore_H264.mp4 to better understand the services we offer.
Nice to have
- Our logo can be redesigned as needed to fix the new look and feel. Brimwood Voice Link is our name but we are willing to change our name to just Brimwood Voice if the name fits the new look and feel.

```html
<!DOCTYPE html>
<html lang="en">
<head>
<meta charset="utf-8">
<title>Brimwood Voice – Hosted PBX</title>
<link href="https://fonts.googleapis.com/css2?family=Arimo:wght@400;700&family=PT+Sans:wght@400&family=Fira+Sans:wght@400&family=Tinos&display=swap" rel="stylesheet">
<style>
:root{
  --page:#eeedea;
  --navy:#1f4a7b;
  --navy-light:#2d6aa6;
  --green:#5fb41b;
  --green-dark:#4a9a10;
  --brand:#1b63a8;
  --ink:#1a1a1a;
  --heading:#1d3f6e;
  --body-blue:#2a4f8f;
  --rule:#e3e3e3;
  --white:#ffffff;
}
*{margin:0;padding:0;box-sizing:border-box}
html,body{width:679px;height:1200px;overflow:hidden}
body{position:relative;background:var(--page);font-family:"Arimo",Arial,sans-serif;color:var(--ink)}
.abs{position:absolute}
.logo{left:33px;top:16px;font:700 20px/1 "Arimo",sans-serif;color:var(--brand);display:flex;align-items:center;gap:5px}
.logo .dot{width:8px;height:8px;border-radius:50%;background:var(--brand)}
.hero{left:0;top:82px;width:679px;height:218px;background:radial-gradient(ellipse at 55% 45%,var(--navy-light),var(--navy) 70%)}
.nav{left:40px;top:68px;width:604px;height:33px;background:var(--white);border-radius:0 0 6px 6px;box-shadow:0 1px 2px rgba(0,0,0,.25);z-index:3}
.nav a{position:absolute;top:11px;font-size:11px;color:var(--ink);text-decoration:none}
.nav .current{top:-2px;height:43px;padding:12px 9px 0;background:var(--green)}
.hero-title{left:70px;top:128px;font:26px/1 "Tinos",serif;color:var(--green);z-index:2}
.hero-line{left:70px;font:16px/1 "Tinos",serif;color:var(--white);z-index:2;white-space:nowrap}
.badge{left:75px;top:225px;width:167px;height:44px;background:var(--white)}
.btn-more{left:262px;top:230px;width:121px;height:34px;border-radius:5px;background:linear-gradient(var(--green),var(--green-dark));color:var(--white);font:13px/34px "Tinos",serif;text-align:center}
.hero-photo{left:448px;top:142px;width:162px;height:130px;border-radius:40px 60px 20px 30px;background:radial-gradient(circle at 45% 45%,#3a3a3a,#1b1b1b 60%,transparent 72%)}
.arrow{width:28px;height:28px;border-radius:50%;background:var(--white);top:180px}
.panel{background:var(--white)}
.video{left:20px;top:320px;width:273px;height:204px;background:#e4e6ea}
.video-art{left:0;top:0;width:273px;height:185px;background:radial-gradient(circle at 40% 55%,#cfd6dd,#eef0f2 60%)}
.video-bar{left:0;top:185px;width:273px;height:19px;background:#dadada}
.welcome h2{left:315px;top:332px;font:400 15px/1 "Fira Sans",sans-serif;color:var(--heading)}
.welcome p{left:314px;width:340px;font:9.2px/16px "PT Sans",sans-serif;color:var(--body-blue)}
.feature h3{left:26px;font:400 10.5px/1 "Arimo",sans-serif;color:var(--heading);z-index:2}
.feature .pic{left:30px;width:114px;height:86px;background:radial-gradient(circle,#9aa0a6,#f4f4f4 70%)}
.feature .divider{left:150px;width:1px;height:90px;background:var(--rule)}
.feature p{left:174px;width:256px;font-size:8.9px;line-height:11.9px;letter-spacing:-.05px}
.hr{left:30px;width:388px;height:1px;background:var(--rule)}
.more-title{left:35px;top:955px;font-size:10.5px;color:var(--heading)}
.more-list{left:44px;top:982px;list-style:none;font-size:8.6px}
.more-list li{height:23px;position:relative;padding-left:16px}
.more-list li::before{content:"";position:absolute;left:0;top:3px;width:4px;height:4px;background:var(--navy)}
.side-title{font-size:10.5px;letter-spacing:.2px}
.services{left:460px;top:593px;list-style:none;font-size:10px}
.services li{height:23px;display:flex;align-items:flex-start;gap:7px}
.services svg{margin-top:2px}
.side-rule{left:452px;width:190px;height:1px;background:#bbb}
.email{left:452px;top:795px;width:185px;height:30px;border-radius:15px;background:#595959;color:#eee;font-size:10px;line-height:30px;padding:0 13px}
.email b{float:right;font-size:9px}
.social{top:880px;display:flex;align-items:center;gap:6px;font-size:10px;font-weight:700}
.social .ico{width:24px;height:24px;border-radius:50%}
.footer{left:0;top:1113px;width:679px;height:87px;background:var(--navy);color:var(--white);text-align:center;font-size:8.5px}
.footer nav{margin-top:29px}
.footer p{margin-top:7px}
</style>
</head>
<body>
<div class="abs logo"><span class="dot"></span>Brimwood Voice</div>

<section class="abs hero"></section>
<nav class="abs nav">
  <a class="current" style="left:20px">Home</a>
  <a style="left:82px">Benefits</a>
  <a style="left:147px">Equipment</a>
  <a style="left:221px">Features</a>
  <a style="left:287px">Partners</a>
  <a style="left:351px">Request a Quote</a>
  <a style="left:456px">FAQ</a>
</nav>
<div class="abs hero-photo" role="img" aria-label="Black desk phone"></div>
<div class="abs hero-title">Introducting</div>
<div class="abs hero-line" style="top:166px">The Brimwood Voice Phone Suite of Business Solutions</div>
<div class="abs hero-line" style="top:194px">VOIP Hosted PBX for your business.</div>
<div class="abs badge" role="img" aria-label="Authorized reseller badge"></div>
<div class="abs btn-more">VIEW MORE</div>
<svg class="abs arrow" style="left:12px" viewBox="0 0 28 28"><path d="M16 9l-5 5 5 5" fill="none" stroke="#5fb41b" stroke-width="3"/></svg>
<svg class="abs arrow" style="left:637px" viewBox="0 0 28 28"><path d="M12 9l5 5-5 5" fill="none" stroke="#5fb41b" stroke-width="3"/></svg>

<section class="abs panel" style="left:10px;top:310px;width:657px;height:229px"></section>
<div class="abs video">
  <div class="abs video-art" role="img" aria-label="Video still: businessman on a sofa with a phone, 'make calls from any device'"></div>
  <div class="abs video-bar">
    <svg width="273" height="19"><rect x="8" y="7" width="214" height="5" rx="2.5" fill="#1d4fa0"/><rect x="234" y="6" width="2" height="7" fill="#222"/><rect x="238" y="6" width="2" height="7" fill="#222"/><path d="M246 6l6 3.5-6 3.5z" fill="#222"/><rect x="258" y="6" width="7" height="7" fill="#222"/></svg>
  </div>
</div>
<div class="welcome">
  <h2 class="abs">WELCOME TO OUR WEBSITE</h2>
  <p class="abs" style="top:362px">Lorem Ipsum is simply dummy text of the printing and typesetting industry. Lorem Ipsum has been the industry's standard dummy text ever since the 1500s, when an unknown printer took a galley of type and scrambled it to make a type specimen book. It has survived not only five centuries, but also the leap into electronic type-setting, remaining essentially unchanged. It was popularised in the 1960s with</p>
  <p class="abs" style="top:456px">Lorem Ipsum is simply dummy text of the printing and typesetting industry. Lorem Ipsum has been the industry's standard dummy text ever since the 1500s, when an unknown printer took a galley of type and scrambled it to make a type specimen book.</p>
</div>

<section class="abs panel" style="left:10px;top:545px;width:423px;height:554px"></section>
<div class="feature">
  <h3 class="abs" style="top:557px">Hosted PBX Benefits</h3>
  <div class="abs pic" style="top:578px" role="img" aria-label="Computer monitor with desk phone"></div>
  <div class="abs divider" style="top:576px"></div>
  <p class="abs" style="top:577px">Lorem Ipsum is simply dummy text of the printing and typeset-ting industry. Lorem Ipsum has been the industry's standard dummy text ever since the 1500s, when an unknown printer took a galley of type and scrambled it to make a type specimen book. It has survived not only five centuries, but also the leap into electronic typesetting, remaining essentially unchanged. It was popularised in the.</p>
</div>
<div class="abs hr" style="top:679px"></div>
<div class="feature">
  <h3 class="abs" style="top:692px">Equipments</h3>
  <div class="abs pic" style="top:708px" role="img" aria-label="Office desk phone"></div>
  <div class="abs divider" style="top:700px"></div>
  <p class="abs" style="top:701px">Lorem Ipsum is simply dummy text of the printing and typeset-ting industry. Lorem Ipsum has been the industry's standard dummy text ever since the 1500s, when an unknown printer took a galley of type and scrambled it to make a type specimen book. It has survived not only five centuries, but also the leap into electronic typesetting, remaining essentially unchanged. It was popularised in the.</p>
</div>
<div class="abs hr" style="top:808px"></div>
<div class="feature">
  <h3 class="abs" style="top:822px">Advanced VoIP Services</h3>
  <div class="abs pic" style="top:838px" role="img" aria-label="Computers, phone and network devices"></div>
  <div class="abs divider" style="top:829px"></div>
  <p class="abs" style="top:830px">Lorem Ipsum is simply dummy text of the printing and typeset-ting industry. Lorem Ipsum has been the industry's standard dummy text ever since the 1500s, when an unknown printer took a galley of type and scrambled it to make a type specimen book. It has survived not only five centuries, but also the leap into electronic typesetting, remaining essentially unchanged. It was popularised in the.</p>
</div>
<div class="abs hr" style="top:944px"></div>
<div class="abs more-title">Read More</div>
<ul class="abs more-list">
  <li>Lorem Ipsum is simply dummy text of the printing and typesetting industry.</li>
  <li>Lorem Ipsum is simply dummy text of the printing and typesetting industry.</li>
  <li>Lorem Ipsum is simply dummy text of the printing and typesetting industry.</li>
  <li>Lorem Ipsum is simply dummy text of the printing and typesetting industry.</li>
  <li>Lorem Ipsum is simply dummy text of the printing and typesetting industry.</li>
</ul>

<section class="abs panel" style="left:439px;top:545px;width:227px;height:198px"></section>
<div class="abs side-title" style="left:460px;top:565px">DATA CENTER SERVICES</div>
<ul class="abs services">
  <li><svg width="10" height="8" viewBox="0 0 10 8"><path d="M0 4h8M5 1l3 3-3 3" fill="none" stroke="#1a1a1a" stroke-width="1.2"/></svg>Backup</li>
  <li><svg width="10" height="8" viewBox="0 0 10 8"><path d="M0 4h8M5 1l3 3-3 3" fill="none" stroke="#1a1a1a" stroke-width="1.2"/></svg>Colocation</li>
  <li><svg width="10" height="8" viewBox="0 0 10 8"><path d="M0 4h8M5 1l3 3-3 3" fill="none" stroke="#1a1a1a" stroke-width="1.2"/></svg>Consultation</li>
  <li><svg width="10" height="8" viewBox="0 0 10 8"><path d="M0 4h8M5 1l3 3-3 3" fill="none" stroke="#1a1a1a" stroke-width="1.2"/></svg>Disaster Recovery</li>
  <li><svg width="10" height="8" viewBox="0 0 10 8"><path d="M0 4h8M5 1l3 3-3 3" fill="none" stroke="#1a1a1a" stroke-width="1.2"/></svg>Facility Overview</li>
  <li><svg width="10" height="8" viewBox="0 0 10 8"><path d="M0 4h8M5 1l3 3-3 3" fill="none" stroke="#1a1a1a" stroke-width="1.2"/></svg>Virtualization</li>
</ul>

<section class="abs panel" style="left:439px;top:750px;width:227px;height:182px"></section>
<div class="abs side-title" style="left:452px;top:759px">NEWSLETTER</div>
<div class="abs side-rule" style="top:778px"></div>
<div class="abs email">Email<b>Submit &gt;&gt;</b></div>
<div class="abs side-title" style="left:452px;top:850px">FOLLOW US ON</div>
<div class="abs side-rule" style="top:869px"></div>
<div class="abs social" style="left:454px"><span class="ico" style="background:#2b5a9a"></span>Friendlio</div>
<div class="abs social" style="left:539px"><span class="ico" style="background:#4fb6e3"></span>Chirplet</div>

<footer class="abs footer">
  <nav>Home &nbsp;|&nbsp; Benefits &nbsp;|&nbsp; Equipment &nbsp;|&nbsp; Features &nbsp;|&nbsp; Partners &nbsp;|&nbsp; Request a Quote &nbsp;|&nbsp; FAQ</nav>
  <p>Copyright © 2011 Suite</p>
</footer>
</body>
</html>
```